Dietetic office: Bright Plate

I want to give my business card a modern and warm look (which attracts the eye and has a reassuring side), which links dietetics to a moment of well-being. The front and back sides must be used (not just to put the logo on the front side)

The map should be eye-catching and easy to read. I don't necessarily want to have a plain background, which I find visually weighs down the maps.
I really like the square format of a business card with rounded edges which is different from what we are used to finding (and why not take this square diagonally?), however I am not closed to another format as long as I like the style.

Who am I? Mireille, 32 years old, Dietician and passionate about food since always. I am specialized in slimming and an expert in micro nutrition, which means that I take into account not only the nutritional balance while maintaining pleasure (if foods are present in the business card, I do not want some cliché things where there would just be fruits and vegetables, but really something more global), but also the psycho-emotional dimension that I will treat with food supplements based on plants, fruits or vegetables.

-----------------------------------------------------------------------------------

 Mention to appear on the card IN FRENCH (please be careful in case of translation that the use of words is correct):

Mireille DORAN
Dietician Nutritionist
Expert in Slimming and Micro-Nutrition

Slogan: I help you lose weight sustainably with pleasure and by reconciling your events

Catchphrases: Want to lose weight? Do you like going out? Do you have a lot of events? And is pleasure on your plate important to you?

Make an appointment on Rendiplan or on 06 41 58 30 92
mireille.brightplate@exemplo-mail.fr
Address: Health Center, Rue des Glycines, 13460 Valbrune
www.brightplate-exemple.fr
Friendwall + Picturo Logo

- The company logo has been uploaded for your viewing. Other file formats can be made available if required.
- I would like a place for a photo of me to be possible.

Good morning,
I want to have a business card that is both lively and warm. Which will easily catch the eye while being easy to read and make people understand that I am in the field of well-being.
I like the square side in business cards (and why not use them diagonally?), or a more classic but original one.
Both the front and back sides must be used (I don't want to have the logo on just one side)
I don't want to have a plain background, but rather something more muted (I really like the suggestion from "Reed Cloud Graphic Designer" for this)
the use of logo for telephone, mail, address, rendiplan, friendwall, pictu etc is possible in order to facilitate reading

Please follow the various elements of the brief regarding the text and use the French text as it is.

I like business cards preferably square (with the possibility of using them diagonally).
The map should be eye-catching and easy to read.
It must bring pep while having softness which brings back to the well-being side
The card must be used on the front and back for the different elements (I do not want to have only the logo on the front side)
The text must correspond to the brief (be careful with the translation which can sometimes be bad)
I don't want to have a plain blue or orange background. I really like the idea of the background from "Reed Cloud Graphic Designer"

You can if you wish use symbols for contacts, telephone, rendiplan, address, fw, pictu....

Target Market(s)

mainly women between 25 and 65 years old + men around 40 years old

Contact Information for Business Card

Font styles to use
Sans Serif
Script

Colors
0054AA
0677BA
7BADD7
CADEEF
E8F1F8
0094D4
00A9DD
6FCCEA
C7EBF8
E9F6FB
00AB8E
00BBA5
67D7C9
C6EFE9
E9F9F6
FFC000
F8CF3A
FAE287
FDF2CF
FEFAEE
F0912C
F2A743
F7CA91
FBE8D2
FDF5EE

Requirements
Must have
• some pep! while being refined
Nice to have
• I really like the square format of a business card with rounded edges which is different from what we are used to finding, however I am not closed to another format as long as I like the style.
Should not have
• if foods are represented, only show fruits and vegetables (too cliché)

```html
<!DOCTYPE html>
<html lang="en">
<head>
<meta charset="utf-8">
<title>Bright Plate – Business Card</title>
<link rel="stylesheet" href="https://fonts.googleapis.com/css2?family=Kaushan+Script&family=Roboto:wght@400;500;700&display=swap">
<style>
  :root {
    --page: #e9e6e2;
    --card-dark: #1c1c1c;
    --gold: #8a7436;
    --gold-soft: #6f5d2a;
    --white: #ffffff;
    --blue: #0a7fd8;
    --blue-name: #0677ba;
    --orange: #f0912c;
    --ink: #111111;
    --ink-soft: #333333;
    --radius: 30px;
  }
  * { box-sizing: border-box; margin: 0; padding: 0; }
  html, body { width: 1200px; height: 872px; overflow: hidden; }
  body {
    background: var(--page);
    font-family: "Roboto", Arial, sans-serif;
    position: relative;
  }
  .card {
    position: absolute;
    width: 700px;
    height: 400px;
    border-radius: var(--radius);
    overflow: hidden;
  }

  /* Back side */
  .card--back {
    left: 420px; top: 30px;
    background: var(--card-dark);
  }
  .back-brand {
    position: absolute;
    left: 150px; top: 90px;
    display: flex; align-items: center; gap: 16px;
    white-space: nowrap;
  }
  .back-brand .brand-dot {
    width: 30px; height: 30px; border-radius: 50%;
    background: var(--gold-soft);
  }
  .back-brand .brand-name {
    font-weight: 400;
    font-size: 68px;
    color: var(--gold);
    letter-spacing: 1px;
  }
  .back-tagline {
    position: absolute; left: 360px; top: 182px;
    font-size: 13px; color: var(--gold-soft);
  }
  .catchphrase {
    position: absolute; left: 40px; top: 230px; width: 630px;
    font-family: "Kaushan Script", cursive;
    font-size: 19px; line-height: 1.45;
    color: var(--gold);
    text-align: center;
  }

  /* Front side */
  .card--front {
    left: 80px; top: 442px;
    background: var(--white);
    display: flex;
  }
  .contact-panel {
    width: 46%;
    padding: 46px 0 0 40px;
    position: relative;
  }
  .accent-bar {
    position: absolute; left: 28px; top: 50px;
    width: 4px; height: 34px; background: var(--orange);
  }
  .person-name {
    font-family: "Kaushan Script", cursive;
    font-weight: 400;
    font-size: 32px; color: var(--blue-name);
    line-height: 1.1;
    white-space: nowrap;
  }
  .person-role {
    font-size: 15px; font-weight: 500; color: var(--ink); margin-top: 4px;
  }
  .person-expertise {
    font-size: 12px; color: var(--ink-soft); margin-top: 2px;
  }
  .contact-list { list-style: none; margin-top: 14px; }
  .contact-list li {
    display: flex; align-items: flex-start; gap: 10px;
    font-size: 13px; color: var(--ink); margin-bottom: 8px;
    white-space: nowrap;
  }
  .contact-list .address { font-size: 11px; color: var(--ink-soft); line-height: 1.35; }
  .contact-list .phone { font-size: 16px; }
  .contact-icon { width: 18px; height: 18px; flex: none; }

  .brand-panel {
    width: 54%;
    background: var(--blue);
    position: relative;
    padding: 130px 24px 0 44px;
  }
  .front-brand { display: flex; align-items: center; gap: 12px; white-space: nowrap; }
  .front-brand .brand-dot {
    width: 24px; height: 24px; border-radius: 50%; background: var(--orange);
  }
  .front-brand .brand-name {
    font-weight: 400; font-size: 42px; color: var(--white);
  }
  .front-tagline {
    font-size: 11px; color: #cfe6f8; margin: 2px 0 0 150px;
    white-space: nowrap;
  }
  .slogan {
    font-family: "Kaushan Script", cursive;
    font-size: 15px; line-height: 1.4; color: var(--white);
    margin-top: 14px; width: 300px;
  }
</style>
</head>
<body>

<section class="card card--back" aria-label="Business card back">
  <div class="back-brand">
    <span class="brand-dot"></span>
    <span class="brand-name">Bright Plate</span>
  </div>
  <p class="back-tagline">La clé de votre bien être</p>
  <p class="catchphrase">Want to lose weight? Do you like going out? Do you have a lot of events?<br>And the pleasure on your plate is important to you?</p>
</section>

<section class="card card--front" aria-label="Business card front">
  <div class="contact-panel">
    <span class="accent-bar"></span>
    <h1 class="person-name">Mireille DORAN</h1>
    <p class="person-role">Dietician Nutritionist</p>
    <p class="person-expertise">Expert in Slimming and Micro-Nutrition</p>
    <ul class="contact-list">
      <li class="address">
        <svg class="contact-icon" viewBox="0 0 20 20"><circle cx="10" cy="10" r="9" fill="none" stroke="#0677ba" stroke-width="1.5"/><path d="M5 10.5 10 6l5 4.5V14H5z" fill="#0677ba"/></svg>
        <span>Health Center, Rue des Glycines,<br>13460 Valbrune</span>
      </li>
      <li class="phone">
        <svg class="contact-icon" viewBox="0 0 20 20"><circle cx="10" cy="10" r="9" fill="none" stroke="#0677ba" stroke-width="1.5"/><path d="M7 5.5c.6 0 1.6 2 1.4 2.5l-.8.9c.6 1.4 1.6 2.4 3 3l.9-.8c.5-.2 2.5.8 2.5 1.4 0 .8-1 1.8-1.8 1.8C9.3 14.3 5.7 10.7 5.2 7.3 5.2 6.5 6.2 5.5 7 5.5z" fill="#0677ba"/></svg>
        <span>06 41 58 30 92</span>
      </li>
      <li>
        <svg class="contact-icon" viewBox="0 0 20 20"><circle cx="10" cy="10" r="9" fill="none" stroke="#0677ba" stroke-width="1.5"/><rect x="5" y="6.5" width="10" height="7" fill="none" stroke="#0677ba" stroke-width="1.4"/><path d="M5 6.5l5 4 5-4" fill="none" stroke="#0677ba" stroke-width="1.4"/></svg>
        <span>mireille.brightplate@exemplo-mail.fr</span>
      </li>
      <li>
        <svg class="contact-icon" viewBox="0 0 20 20"><circle cx="10" cy="10" r="9" fill="none" stroke="#0677ba" stroke-width="1.5"/><circle cx="10" cy="10" r="5.5" fill="none" stroke="#0677ba" stroke-width="1.2"/><path d="M4.5 10h11M10 4.5c-2.5 3-2.5 8 0 11M10 4.5c2.5 3 2.5 8 0 11" fill="none" stroke="#0677ba" stroke-width="1.1"/></svg>
        <span>www.brightplate-exemple.fr</span>
      </li>
    </ul>
  </div>

  <div class="brand-panel">
    <div class="front-brand">
      <span class="brand-dot"></span>
      <span class="brand-name">Bright Plate</span>
    </div>
    <p class="front-tagline">La clé de votre bien être</p>
    <p class="slogan">I help you lose weight sustainably with pleasure and by reconciling your events.</p>
  </div>
</section>

</body>
</html>
```